Book Cover for a technology book - The Silent Lattice

We are writing a book that is a handbook how to build a hybrid cloud - this is a technology concept where companies use cloud services both from the like of Vornix or Plenquor and also cloud services built in there own data centers - hence the term hybrid cloud. We want a book cover with the title - The Silent Lattice; which signifies that we will be teaching companies how to build a hybrid cloud that just works. We want the tagline - handbook for building Hybrid Clouds. The authors are Corwin Haddle and Ross Pelley. The cover is to be engaging and feel different than your usual technical manual. I don't have any graphics to help out however will be able to refine and tell you what I don and don't like based on your drafts. The book dimensions are yet to be determined, in the first instance it will be a PDF

Target Market(s)

technology executives and specialists

Industry/Entity Type

Information Technology

Colors

Designer to choose colors to be used in the design.

Requirements
Nice to have
• While I don't have a particular view to how it will look, I'd like the style to be more casual than ultra formal

```html
<!DOCTYPE html>
<html lang="en">
<head>
<meta charset="utf-8">
<title>The Silent Lattice – Book Cover</title>
<link rel="stylesheet" href="https://fonts.googleapis.com/css2?family=Montserrat:ital,wght@1,400;1,800;1,900&display=swap">
<style>
  :root {
    --backdrop: #000000;
    --paper: #ffffff;
    --ink: #0b0b0b;
    --sky-light: #5cc4ea;
    --sky-mid: #45aee0;
    --sky-deep: #3a8fd0;
    --band-blue: #1b4aa0;
  }
  * { margin: 0; padding: 0; box-sizing: border-box; }
  html, body {
    width: 1200px;
    height: 1199px;
    overflow: hidden;
    background: var(--backdrop);
  }
  .canvas {
    position: relative;
    width: 1200px;
    height: 1199px;
    background: var(--backdrop);
  }
  .cover {
    position: absolute;
    left: 237px;
    top: 87px;
    width: 726px;
    height: 1025px;
    background: var(--paper);
    overflow: hidden;
  }
  .cover-art {
    position: absolute;
    inset: 0;
    width: 726px;
    height: 1025px;
  }
  .title {
    position: absolute;
    left: 0;
    top: 310px;
    width: 726px;
    text-align: center;
    transform: rotate(-7deg);
    font-family: "Montserrat", sans-serif;
    font-style: italic;
    font-weight: 900;
    text-transform: uppercase;
    line-height: 1;
  }
  .title-lead {
    display: block;
    font-size: 88px;
    color: var(--ink);
    letter-spacing: -1px;
    text-shadow: 3px 3px 0 var(--paper);
  }
  .title-main {
    display: block;
    margin-top: 10px;
    font-size: 150px;
    color: var(--paper);
    letter-spacing: -3px;
    text-shadow:
      2px 2px 0 var(--ink), 4px 4px 0 var(--ink), 6px 6px 0 var(--ink),
      8px 8px 0 var(--ink), 10px 10px 0 var(--ink), 12px 12px 0 var(--ink);
  }
  .tagline {
    position: absolute;
    left: 0;
    top: 606px;
    width: 726px;
    text-align: center;
    transform: rotate(-7deg);
    font-family: "Montserrat", sans-serif;
    font-style: italic;
    font-weight: 800;
    text-transform: uppercase;
    color: var(--paper);
    line-height: 0.98;
  }
  .tagline-line { display: block; font-size: 72px; letter-spacing: -0.5px; }
  .tagline-line.is-large { font-size: 94px; letter-spacing: -1px; }
  .authors {
    position: absolute;
    left: 0;
    top: 925px;
    width: 726px;
    text-align: center;
    transform: rotate(-6deg);
    font-family: "Montserrat", sans-serif;
    font-style: italic;
    font-weight: 400;
    font-size: 36px;
    color: var(--ink);
  }
</style>
</head>
<body>
<main class="canvas">
  <section class="cover">
    <svg class="cover-art" viewBox="0 0 726 1025" xmlns="http://www.w3.org/2000/svg">
      <defs>
        <linearGradient id="art-fill" x1="0" y1="0" x2="1" y2="1">
          <stop offset="0" stop-color="var(--sky-mid)"/>
          <stop offset="0.5" stop-color="var(--sky-light)"/>
          <stop offset="1" stop-color="var(--sky-deep)"/>
        </linearGradient>
      </defs>
      <rect class="art-placeholder" role="img" aria-label="Area for the faceted blue cloud illustration"
            x="0" y="80" width="726" height="720" fill="url(#art-fill)"/>
      <polygon class="tagline-band" fill="var(--band-blue)" points="0,640 726,543 726,807 0,910"/>
      <rect class="paper-foot" fill="var(--paper)" x="0" y="0" width="0" height="0"/>
    </svg>

    <h1 class="title">
      <span class="title-lead">The Silent</span>
      <span class="title-main">Lattice</span>
    </h1>

    <p class="tagline">
      <span class="tagline-line">Handbook for</span>
      <span class="tagline-line is-large">Building</span>
      <span class="tagline-line">Hybrid Clouds</span>
    </p>

    <p class="authors">Corwin Haddle and Ross Pelley</p>
  </section>
</main>
</body>
</html>
```